New company looking for logo, for business cards and email signature.
we provide Safety, Training and Project Management Services to Mining and Transport sectors.

Industry/Entity Type

Business

Contact Information for Business Card

HARTWELL CONSULTANCY, Owen Fairclough, Principal Consultant, 0491362847, hartwellconsultancy@postvane.com , Unit 214,Corvale Business Hub,517 Tindal Road, Brenmoor, 4812.
Dependable Operations through Safety, Coaching and Direction.

```html
<!DOCTYPE html>
<html lang="en">
<head>
<meta charset="UTF-8">
<title>Hartwell Consultancy – Business Card</title>
<link rel="stylesheet" href="https://fonts.googleapis.com/css2?family=Lato:wght@300;400;700&display=swap">
<style>
  :root {
    --backdrop: #dcdcdc;
    --card: #ffffff;
    --gold: #bd822c;
    --gold-light: #d8a35a;
    --ink: #1d2229;
    --shadow: 0 4px 10px rgba(0,0,0,0.22);
  }
  * { margin: 0; padding: 0; box-sizing: border-box; }
  html, body {
    width: 1200px; height: 1000px; overflow: hidden;
    background: var(--backdrop);
    font-family: "Lato", sans-serif;
  }
  .stage { position: relative; width: 1200px; height: 1000px; }
  .card {
    position: absolute; left: 252px; width: 694px; height: 427px;
    background: var(--card); box-shadow: var(--shadow); overflow: hidden;
  }
  .card--front { top: 53px; }
  .card--back { top: 521px; border-bottom: 2px solid var(--gold); }

  .brand {
    position: absolute; top: 88px; left: 0; width: 100%;
    text-align: center; color: var(--gold);
    font-weight: 400; font-size: 30px; letter-spacing: 2px; line-height: 1;
  }
  .identity {
    position: absolute; top: 181px; left: 0; width: 100%;
    text-align: center; font-size: 19px; color: var(--gold);
  }
  .identity__name { font-weight: 700; }
  .identity__role { font-weight: 300; }
  .divider {
    position: absolute; top: 237px; left: 266px; width: 181px; height: 2px;
    background: var(--gold);
  }
  .contact {
    position: absolute; color: var(--ink); font-size: 17px; line-height: 26px;
  }
  .contact__row { display: flex; align-items: flex-start; gap: 9px; }
  .contact__row + .contact__row { margin-top: 6px; }
  .contact__icon { flex: none; width: 20px; height: 26px; display: flex; align-items: center; justify-content: center; }
  .contact--left { top: 294px; left: 53px; }
  .contact--right { top: 294px; left: 370px; }

  .sweep { position: absolute; left: 0; top: 0; width: 120px; height: 427px; }
  .tagline {
    position: absolute; top: 166px; left: 153px;
    color: var(--gold); font-weight: 300; font-size: 28px; line-height: 40px;
  }
</style>
</head>
<body>
<div class="stage">

  <section class="card card--front">
    <div class="brand">HARTWELL CONSULTANCY</div>
    <div class="identity">
      <span class="identity__name">Owen Fairclough</span> | <span class="identity__role">Principal Consultant</span>
    </div>
    <div class="divider"></div>

    <div class="contact contact--left">
      <div class="contact__row">
        <span class="contact__icon">
          <svg width="14" height="20" viewBox="0 0 14 20"><rect x="1.5" y="1" width="11" height="18" rx="2" fill="none" stroke="var(--gold)" stroke-width="2"/><rect x="5" y="15" width="4" height="1.6" fill="var(--gold)"/></svg>
        </span>
        <span>0491362847</span>
      </div>
      <div class="contact__row">
        <span class="contact__icon">
          <svg width="20" height="14" viewBox="0 0 20 14"><rect x="0" y="0" width="20" height="14" fill="var(--gold)"/><path d="M1 1 L10 8 L19 1" fill="none" stroke="#fff" stroke-width="1.5"/></svg>
        </span>
        <span>hartwellconsultancy@postvane.com</span>
      </div>
    </div>

    <div class="contact contact--right">
      <div class="contact__row">
        <span class="contact__icon">
          <svg width="14" height="20" viewBox="0 0 14 20"><path d="M7 0 C3 0 0 3 0 7 C0 12 7 20 7 20 C7 20 14 12 14 7 C14 3 11 0 7 0 Z" fill="var(--gold)"/><circle cx="7" cy="7" r="2.6" fill="#fff"/></svg>
        </span>
        <span>Unit 214,Corvale<br>Business Hub, 517 Tindal Road,<br>Brenmoor, 4812.</span>
      </div>
    </div>
  </section>

  <section class="card card--back">
    <svg class="sweep" viewBox="0 0 120 427" preserveAspectRatio="none" aria-hidden="true">
      <path d="M0 0 H40 C75 120 92 210 86 280 C80 350 60 395 38 427 H0 Z" fill="var(--gold-light)"/>
      <path d="M0 0 H36 C65 120 80 200 76 270 C72 340 40 395 13 427 H0 Z" fill="var(--gold)"/>
    </svg>
    <p class="tagline">Dependable Operations through Safety,<br>Coaching and Direction</p>
  </section>

</div>
</body>
</html>
```